Business Card Design Project

Hello,

We need a business card, which will be presented the our company Studio Lopatka and its brand Framehaul.
Studio Lopatka is a video production company.
Stock video footage Framehaul is a trademark of Studio Lopatka.
We need a designer that will set both the logo and contacts on the card. Print will be executed on a single page, it will use a translucent paper.

Contacts:

Tadej Bremec
Founder and CEO

Studio Lopatka d.o.o., Pot na Slivnik 14, 8000 Novo mesto, Slovenia
T: +386 599 81 316, M: +386 41 203 659
tadej@lopatka-example.si, www.lopatka-example.si
info@framehaul-example.com, www.framehaul-example.com

In the attachment are located both logo!

Thanks in advance,

Tadej

```html
<!DOCTYPE html>
<html lang="en">
<head>
<meta charset="utf-8">
<title>Studio Lopatka – Business Card</title>
<link rel="stylesheet" href="https://fonts.googleapis.com/css2?family=Arvo:wght@700&display=swap">
<style>
  :root {
    --page-bg: #ececec;
    --card-bg: #ffffff;
    --ink: #111111;
    --mark-dark: #2b2b2b;
  }
  * { margin: 0; padding: 0; box-sizing: border-box; }
  html, body {
    width: 1200px;
    height: 900px;
    overflow: hidden;
    background: var(--page-bg);
  }
  .canvas {
    position: relative;
    width: 1200px;
    height: 900px;
  }
  .card {
    position: absolute;
    left: 100px;
    top: 150px;
    width: 1000px;
    height: 600px;
    background: var(--card-bg);
    font-family: "Arvo", Georgia, serif;
    font-weight: 700;
    color: var(--ink);
  }
  .brand {
    position: absolute;
    top: 40px;
    left: 0;
    width: 100%;
    text-align: center;
  }
  .brand-dot {
    display: block;
    width: 150px;
    height: 150px;
    margin: 0 auto 22px;
    border-radius: 50%;
    background: var(--mark-dark);
  }
  .brand-name {
    font-size: 64px;
    line-height: 1;
    color: var(--ink);
  }
  .person {
    position: absolute;
    left: 28px;
    top: 330px;
  }
  .person-name {
    font-size: 36px;
    line-height: 1.1;
  }
  .person-role {
    font-size: 19px;
    line-height: 1.2;
  }
  .contacts {
    position: absolute;
    top: 440px;
    font-size: 17px;
    line-height: 1.45;
    font-style: normal;
    white-space: nowrap;
  }
  .contacts-address { left: 22px; }
  .contacts-studio  { left: 370px; }
  .contacts-mobile  { left: 690px; }
  .sub-brand {
    position: absolute;
    left: 370px;
    top: 535px;
    display: flex;
    align-items: center;
    gap: 10px;
    font-size: 22px;
  }
  .sub-brand-square {
    width: 24px;
    height: 24px;
    background: var(--mark-dark);
  }
</style>
</head>
<body>
<main class="canvas">
  <article class="card">
    <header class="brand">
      <span class="brand-dot"></span>
      <p class="brand-name">Studio Lopatka</p>
    </header>

    <section class="person">
      <h1 class="person-name">Tadej Bremec</h1>
      <p class="person-role">Founder and CEO</p>
    </section>

    <address class="contacts contacts-address">
      Studio Lopatka d.o.o.<br>
      Pot na Slivnik 14<br>
      8000 Novo mesto, Slovenia
    </address>

    <p class="contacts contacts-studio">
      T: +386 599 81 316<br>
      www.lopatka-example.si<br>
      www.framehaul-example.com
    </p>

    <p class="contacts contacts-mobile">
      M: +386 41 203 659<br>
      tadej@lopatka-example.si<br>
      info@framehaul-example.com
    </p>

    <div class="sub-brand">
      <span class="sub-brand-square"></span>
      <span class="sub-brand-name">Framehaul</span>
    </div>
  </article>
</main>
</body>
</html>
```